Law Firm Needs a Stationery Design

We need a stationery design for a law firm based in the East African region called 'Mbogoreto Lwanyika & Company Advocates'. We are a law firm specializing in commercial, public and constitutional law. Our practice areas include Telecommunications Law, Mining Law, Oil and Energy Law, Real Estate and Land Development Law, Employment Law, Family Law, Civil and Criminal Litigation, Constitutional Law, Company Secretariat and more. We represent a wide variety of clients, ranging from individuals to corporations and approach each case with full attention, dedication and legal acumen in order to protect the interests of our clients. The final stationary design should communicate innovation and expertise to meet our clients’ legal needs.
Target Market(s)
New clients, current and former clients, other lawyers in and outside of our practice area, or other professionals, contacts and centers of influence within the region
Industry/Entity Type
Real Estate
Colors
Designer to choose colors to be used in the design.
Look and feel

```html
<!DOCTYPE html>
<html lang="en">
<head>
<meta charset="utf-8">
<title>Mbogoreto Lwanyika &amp; Company Advocates – Stationery</title>
<link rel="stylesheet" href="https://fonts.googleapis.com/css2?family=Source+Sans+3:wght@400;600&display=swap">
<style>
  :root {
    --maroon: #862d3a;
    --maroon-deep: #6e2230;
    --ink: #5f5f62;
    --ink-soft: #8a8a8d;
    --rule: #b5b5b8;
    --paper: #ffffff;
    --bg: #ffffff;
  }
  * { box-sizing: border-box; margin: 0; padding: 0; }
  html, body { width: 1200px; height: 770px; overflow: hidden; background: var(--bg); }
  body { font-family: "Source Sans 3", "Segoe UI", sans-serif; color: var(--ink); }
  .canvas { position: relative; width: 1200px; height: 770px; }

  .sheet { position: absolute; background: var(--paper); border: 1px solid var(--rule); }
  .label { position: absolute; font-size: 8px; color: #333; }

  .brand-mark {
    position: absolute; left: 50%; transform: translateX(-50%);
    display: flex; align-items: center; gap: 4px; white-space: nowrap;
    color: var(--maroon); font-weight: 600;
  }
  .brand-mark .dot { width: 7px; height: 7px; background: var(--maroon); }
  .firm-name { position: absolute; left: 0; right: 0; text-align: center; color: var(--ink); white-space: nowrap; }
  .contact-line { position: absolute; left: 0; right: 0; text-align: center; color: var(--ink-soft); white-space: nowrap; }

  /* Letterhead */
  .letterhead { left: 64px; top: 86px; width: 424px; height: 600px; }
  .letterhead .brand-mark { top: 36px; font-size: 16px; }
  .letterhead .firm-name { top: 77px; font-size: 14px; }
  .letterhead .contact-line { top: 580px; font-size: 6px; }

  /* Business cards */
  .card-front { left: 240px; top: 246px; width: 183px; height: 104px; }
  .card-front .brand-mark { top: 26px; font-size: 12px; }
  .card-front .firm-name { top: 62px; font-size: 11px; line-height: 13px; white-space: normal; }
  .card-back { position: absolute; left: 443px; top: 246px; width: 181px; height: 104px; background: var(--maroon); color: #fff; text-align: center; }
  .card-back .person { position: absolute; top: 43px; left: 0; right: 0; font-size: 7px; line-height: 9px; }
  .card-back .details { position: absolute; top: 82px; left: 0; right: 0; font-size: 5.5px; line-height: 9px; color: #f0dfe2; }

  /* Envelope front */
  .envelope-front { left: 142px; top: 371px; width: 488px; height: 230px; z-index: 2; }
  .envelope-front .brand-mark { top: 153px; font-size: 16px; }
  .envelope-front .firm-name { top: 193px; font-size: 13px; }
  .envelope-front .contact-line { top: 211px; font-size: 6px; }

  /* Complimentary card */
  .comp-card { left: 654px; top: 84px; width: 307px; height: 188px; }
  .comp-card .brand-mark { top: 20px; font-size: 13px; }
  .comp-card .firm-name { top: 49px; font-size: 11px; }

  /* Open envelope */
  .envelope-open { position: absolute; left: 650px; top: 292px; width: 488px; height: 310px; }

  .concept { position: absolute; right: 25px; top: 735px; font-size: 15px; color: var(--ink); }
</style>
</head>
<body>
<main class="canvas">

  <section class="sheet letterhead" aria-label="Letterhead">
    <div class="brand-mark"><span class="dot"></span>Mbogoreto Lwanyika</div>
    <p class="firm-name">Mbogoreto Lwanyika &amp; Company Advocates</p>
    <p class="contact-line">Address Line, Lorem ipsum dolor sit amet, consectetuer adipiscing &nbsp;T: 12345 12345 E: info@mlca-law.com W: www.mlca-law.com</p>
  </section>
  <p class="label" style="left:64px; top:694px;">Letterhead</p>

  <p class="label" style="left:240px; top:234px;">Business Card (front/back)</p>
  <section class="sheet card-front" aria-label="Business card front">
    <div class="brand-mark"><span class="dot"></span>Mbogoreto Lwanyika</div>
    <p class="firm-name">Mbogoreto Lwanyika<br>&amp; Company Advocates</p>
  </section>
  <section class="card-back" aria-label="Business card back">
    <p class="person">Mbogoreto Lwanyika<br>Principle Lawyer</p>
    <p class="details">Address Line, Lorem ipsum dolor sit amet, consectetuer adipiscing<br>T: 12345 12345 E: info@mlca-law.com W: www.mlca-law.com</p>
  </section>

  <section class="sheet envelope-front" aria-label="Envelope front">
    <div class="brand-mark"><span class="dot"></span>Mbogoreto Lwanyika</div>
    <p class="firm-name">Mbogoreto Lwanyika &amp; Company Advocates</p>
    <p class="contact-line">Address Line, Lorem ipsum dolor sit amet, consectetuer adipiscing. T: 12345 12345 E: info@mlca-law.com W: www.mlca-law.com</p>
  </section>
  <p class="label" style="left:142px; top:607px;">Envelope (front/open)</p>

  <section class="sheet comp-card" aria-label="Complimentary card">
    <div class="brand-mark"><span class="dot"></span>Mbogoreto Lwanyika</div>
    <p class="firm-name">Complimentary Card</p>
  </section>
  <p class="label" style="left:894px; top:277px;">Complimentary Slip</p>

  <svg class="envelope-open" viewBox="0 0 488 310" aria-label="Envelope open">
    <defs>
      <linearGradient id="flapShade" x1="0" y1="0" x2="0" y2="1">
        <stop offset="0" stop-color="#5e1c28"/>
        <stop offset="0.35" stop-color="#862d3a"/>
        <stop offset="1" stop-color="#862d3a"/>
      </linearGradient>
    </defs>
    <rect x="0.5" y="78" width="487" height="231" fill="#fff" stroke="#b5b5b8"/>
    <path d="M0 78 V26 Q0 0 26 0 H462 Q488 0 488 26 V78 Z" fill="#862d3a"/>
    <path d="M25 78 L42 132 Q47 150 62 151 H426 Q441 150 446 132 L463 78 Z" fill="url(#flapShade)"/>
  </svg>

  <p class="concept">Concept: In the symbol ML depicts brand name as well as showing scale of justice</p>
</main>
</body>
</html>
```